Dubai Family protection infographic

We need to produce a way of attracting people to a life insurance and critical illness cover seminar. As this is a pretty dull subject for most people, so we need a cool way of getting people to read the invite/marketing collateral.

We're thinking some kind of colourful and attractive infographic that we can use on flyers and posters as well as online and as an emailer.

Content for the graphic is as bellow:

How much does it cost to replace Mum & Dad?

Mum = Chauffer, Cook, Laundry Service, Household Cleaner, Psychologist, Money Manager

Mums typically work a 94-hour week. At a rather paltry $12 per hour, that’s $4,888 per month – or $58,656 each year. (Source: wagelore.net)

Dad : The average Western Expat’s salary in the Gulf is $12,215 per month. That’s $146,580 each year. (Source: Palmcrest Ledger).

Did you know that the average age of critical illness claimants in the Middle East last year was just 48. Of these, 44% were for cancer while 41% were heart related.

The average age of a death claimant was just 50 years old.
(Source: Verenholt Assurance Group)

1 in 3 people will develop some form of cancer during their lifetime.

That’s 2.36 billion people globally.

And that’s equivalent to the population of China, USA, Brazil, Russia, Philippines, France, UK, South Africa and Italy combined.

Does your family have the resources to hand to cope if a tragedy happens to you?

What can you do to protect them and yourself?

Come to the UAE’s first national protection seminar to find out. Join us at Harbourline Riverside Sports Arena on June 19th at 19:00.

To pre-register, visit www.tovanmere.net/events or alternatively register on the door.

```html
<!DOCTYPE html>
<html lang="en">
<head>
<meta charset="utf-8">
<title>How much does it cost to replace Mum &amp; Dad?</title>
<link href="https://fonts.googleapis.com/css2?family=Source+Sans+3:wght@400;600;700;800&display=swap" rel="stylesheet">
<style>
:root{
  --page:#e4e3e3;
  --page-edge:#c9c8c8;
  --sheet:#2f2f2f;
  --band:#454545;
  --footer:#2a2a2a;
  --label:#474747;
  --rule:#6a6a6a;
  --ink:#ffffff;
  --muted:#c2c2c2;
  --soft:#9a9a9a;
  --red:#d9484b;
  --blue:#3fb0d8;
  --orange:#f2a233;
  --green:#6aa35a;
  --figure-grey:#c9c4b6;
}
*{margin:0;padding:0;box-sizing:border-box}
html,body{width:1200px;height:900px;overflow:hidden}
body{
  background:radial-gradient(ellipse at center,#f4f4f4 0%,var(--page) 55%,var(--page-edge) 100%);
  font-family:"Source Sans 3",Arial,sans-serif;
  position:relative;
}
.sheet{position:absolute;left:348px;top:18px;width:504px;height:864px;background:var(--sheet);color:var(--ink);overflow:hidden}
.sheet > *{position:absolute}
.title{left:14px;top:8px;font-size:30px;font-weight:800;letter-spacing:-.3px;line-height:1.2}
.subtitle{left:15px;top:44px;font-size:18px;font-weight:600;color:var(--muted)}
.dollar{left:405px;top:20px;font-size:34px;font-weight:800}
.figure{border-radius:4px}
.divider-band{left:0;top:76px;width:504px;height:10px;background:#3b3b3b}
.box{background:var(--label);color:var(--muted);font-weight:600;font-size:12px;display:block;white-space:nowrap;height:21px;line-height:21px;padding:0 8px}
.box-multi{background:var(--label);color:var(--muted);font-weight:600;font-size:11px;line-height:1.25;padding:5px 8px}
.pill{border-radius:18px;font-weight:700;color:var(--sheet);display:flex;align-items:center;justify-content:center}
.tag{height:21px;font-size:12.5px;font-weight:700;color:var(--ink);display:flex;align-items:center;padding:0 5px;white-space:nowrap}
.green{background:var(--green)} .red{background:var(--red)} .blue{background:var(--blue)} .orange{background:var(--orange)}
.name-pill{height:28px;border-radius:14px;background:var(--label);font-size:14px;font-weight:700;color:var(--muted);display:flex;align-items:center;gap:8px}
.dot{width:24px;height:24px;border-radius:50%;display:inline-block}
.source{font-size:10.5px;color:var(--soft);font-weight:600}
.big-num{font-size:22px}
.hours{left:35px;top:177px;width:72px;height:72px;border-radius:50%;background:var(--orange);color:var(--sheet);display:flex;flex-direction:column;align-items:center;justify-content:center;line-height:.9}
.hours b{font-size:22px;color:var(--ink)} .hours span{font-size:13px;font-weight:700}
.hl-orange{color:var(--orange)} .hl-blue{color:var(--blue)} .hl-white{color:var(--ink)}
.know-title{left:18px;top:364px;font-size:21px;font-weight:800}
.know-text{left:18px;top:389px;font-size:13.5px;font-weight:600;color:var(--muted);line-height:1.25}
.know-text b{font-size:20px;color:var(--blue);font-weight:700}
.donut-val{font-size:9px;font-weight:700;color:var(--ink)}
.billion-circle{left:282px;top:474px;width:76px;height:76px;border-radius:50%;background:var(--blue);display:flex;flex-direction:column;align-items:center;justify-content:center;line-height:.95}
.billion-circle span{font-size:14px;font-weight:600} .billion-circle b{font-size:32px;font-weight:700}
.question{left:20px;font-size:15px;font-weight:600;color:var(--muted);line-height:1.1;white-space:nowrap}
.question em{font-style:normal;font-size:22px;font-weight:800;color:var(--blue)}
.question strong{color:var(--ink);font-weight:700}
.family{left:336px;top:618px;width:140px;height:94px;border-radius:6px;background:linear-gradient(90deg,var(--blue),var(--red) 40%,var(--blue) 70%,var(--red))}
.invite{left:0;top:722px;width:504px;height:76px;background:var(--band);text-align:center}
.invite p{font-weight:700}
.invite .lead{color:var(--orange);font-size:16px;margin-top:6px}
.invite .venue{font-size:17.5px;line-height:1.25;margin-top:3px;font-weight:600}
.register{left:0;top:798px;width:504px;height:66px;background:var(--footer);text-align:center;font-size:17.5px;font-weight:600;line-height:1.25;padding-top:10px}
.register a{color:var(--blue);text-decoration:none}
</style>
</head>
<body>
<main class="sheet">
  <h1 class="title">How much does it cost</h1>
  <p class="subtitle">to replace Mum &amp; Dad?</p>
  <div class="figure blue" style="left:382px;top:20px;width:20px;height:44px" role="img" aria-label="Male figure pictogram"></div>
  <span class="dollar">$</span>
  <div class="figure red" style="left:438px;top:20px;width:22px;height:44px" role="img" aria-label="Female figure pictogram"></div>
  <div class="divider-band"></div>

  <svg style="left:0;top:90px" width="504" height="180" viewBox="0 0 504 180">
    <line x1="96" y1="24" x2="174" y2="24" stroke="var(--rule)" stroke-width="2"/>
    <polyline points="7,128 42,146 490,154" fill="none" stroke="var(--rule)" stroke-width="1.5"/>
  </svg>
  <div class="name-pill" style="left:14px;top:100px;width:82px;padding-left:2px"><span class="dot red"></span>Mum</div>
  <div class="pill orange" style="left:120px;top:99px;width:30px;height:30px;border-radius:50%;color:var(--ink);font-size:20px">=</div>
  <div class="tag green" style="left:174px;top:102px">Chauffer</div>
  <div class="tag red" style="left:240px;top:102px">Cook</div>
  <div class="tag blue" style="left:286px;top:102px">Laundry service</div>
  <div class="tag orange" style="left:391px;top:102px">Psychologist</div>
  <div class="tag red" style="left:174px;top:129px">Household Cleaner</div>
  <div class="tag green" style="left:293px;top:129px">Money Manager</div>
  <div class="figure red" style="left:18px;top:135px;width:20px;height:47px" role="img" aria-label="Mum figure pictogram"></div>
  <p style="left:50px;top:134px;font-size:14px;font-weight:600;color:var(--muted);line-height:1.15">Typically<br>works a ...</p>
  <div class="hours"><b>94 Hr</b><span>week</span></div>
  <div class="box-multi" style="left:110px;top:178px;width:104px;height:40px">At a rather paltry<br><span class="hl-orange">$12 per hour</span></div>
  <p class="source" style="left:114px;top:224px">(Source: wagelore.net)</p>
  <div class="box" style="left:232px;top:169px;width:50px">That’s</div>
  <div class="pill blue big-num" style="left:280px;top:162px;width:102px;height:32px">$4,888</div>
  <div class="box" style="left:382px;top:169px;width:74px">per month</div>
  <div class="box" style="left:232px;top:208px;width:50px">Or</div>
  <div class="pill red big-num" style="left:282px;top:200px;width:110px;height:36px">$58,656</div>
  <div class="box" style="left:392px;top:208px;width:66px">each year</div>

  <div class="box-multi" style="left:20px;top:266px;width:158px;height:38px">The average Western Expat’s<br>salary in the Gulf is ...</div>
  <p class="source" style="left:21px;top:311px">(Source: Palmcrest Ledger)</p>
  <div class="pill orange big-num" style="left:197px;top:267px;width:98px;height:32px">$12,215</div>
  <div class="box" style="left:295px;top:273px;width:70px">per month</div>
  <div class="box" style="left:192px;top:310px;width:34px">Or</div>
  <div class="pill green big-num" style="left:224px;top:304px;width:104px;height:32px;color:var(--ink)">$146,580</div>
  <div class="box" style="left:328px;top:310px;width:64px">each year</div>
  <div class="name-pill" style="left:404px;top:258px;width:74px;padding-left:12px;gap:10px">Dad<span class="dot blue"></span></div>
  <div class="figure blue" style="left:432px;top:294px;width:18px;height:46px" role="img" aria-label="Dad figure pictogram"></div>

  <svg style="left:0;top:349px" width="504" height="2"><line x1="0" y1="1" x2="494" y2="1" stroke="var(--rule)" stroke-width="1.5"/></svg>

  <h2 class="know-title">Did you know</h2>
  <p class="know-text">that the average age of critical illness claiments<br>in the Middle East last year was just <b>48.</b></p>
  <div class="box" style="left:12px;top:435px;width:312px;font-size:11px">The average age of a death claimant was just <span class="hl-orange">50</span> year old.</div>
  <svg style="left:270px;top:358px" width="130" height="120" viewBox="0 0 130 120">
    <line x1="0" y1="50" x2="62" y2="38" stroke="var(--rule)"/>
    <line x1="0" y1="50" x2="62" y2="80" stroke="var(--rule)"/>
    <circle cx="85" cy="25" r="17" fill="none" stroke="#5a3333" stroke-width="10"/>
    <circle cx="85" cy="25" r="17" fill="none" stroke="var(--red)" stroke-width="10" stroke-dasharray="47 107" transform="rotate(-90 85 25)"/>
    <circle cx="85" cy="75" r="17" fill="none" stroke="#5a4426" stroke-width="10"/>
    <circle cx="85" cy="75" r="17" fill="none" stroke="var(--orange)" stroke-width="10" stroke-dasharray="44 107" transform="rotate(-90 85 75)"/>
    <text x="85" y="28" text-anchor="middle" class="donut-val" fill="#fff">44%</text>
    <text x="85" y="78" text-anchor="middle" class="donut-val" fill="#fff">41%</text>
  </svg>
  <div class="box" style="left:385px;top:369px;height:23px;line-height:23px">Were for Cancer</div>
  <div class="box" style="left:385px;top:419px;height:23px;line-height:23px">Were heart related</div>
  <p class="source" style="left:396px;top:452px;text-align:center;line-height:1.15">(Source: Verenholt<br>Assurance Group)</p>

  <div class="figure" style="left:14px;top:476px;width:20px;height:46px;background:var(--figure-grey)" role="img" aria-label="Person pictogram"></div>
  <div class="figure" style="left:40px;top:476px;width:20px;height:46px;background:var(--figure-grey)" role="img" aria-label="Person pictogram"></div>
  <div class="figure red" style="left:66px;top:476px;width:20px;height:46px" role="img" aria-label="Person pictogram highlighted"></div>
  <div class="box" style="left:118px;top:478px;width:96px;height:22px;line-height:22px;border-radius:0 12px 12px 0;padding-left:18px;font-size:14px">in 3 people</div>
  <div class="pill red" style="left:104px;top:477px;width:24px;height:24px;border-radius:50%;color:var(--ink);font-size:16px">1</div>
  <p style="left:104px;top:508px;font-size:12px;font-weight:600;color:var(--muted);line-height:1.15">will develop some form of cancer<br>during their lifetime</p>
  <div class="billion-circle"><span>That’s</span><b>2.3</b></div>
  <p style="left:364px;top:487px;font-size:25px;font-weight:700">billion</p>
  <p style="left:364px;top:514px;font-size:18px;font-weight:600;color:var(--muted)">people globally</p>
  <div style="left:18px;top:540px;width:136px;height:54px;background:linear-gradient(90deg,#3a3a3a,#353535);border-radius:10px" role="img" aria-label="World map silhouette"></div>
  <div class="box-multi" style="left:146px;top:557px;width:344px;height:36px;color:var(--muted)">And that’s the equivalent to the population of <span class="hl-white">China, USA, Brazil,</span><br><span class="hl-white">Russia, Phillippines, France, UK, South Africa</span> and <span class="hl-white">Italy</span> <span class="hl-blue">combined.</span></div>

  <p class="question" style="top:612px"><em>Does your family</em> have the resources<br>to hand to cope if a tradgedy happens to <strong>you?</strong></p>
  <p class="question" style="top:662px"><em>What</em> can you do to protect them<br>and yourself?</p>
  <div class="family" role="img" aria-label="Family pictogram: two parents and two children"></div>

  <section class="invite">
    <p class="lead">Come to the UAE’s first national protection seminar to find out.</p>
    <p class="venue">Join us at Harbourline Riverside Sports Arena<br>on June 19th at 19:00</p>
  </section>
  <section class="register">
    <p>To pre-register, visit <a href="#">www.tovanmere.net/events</a><br>or alternatively register on the door.</p>
  </section>
</main>
</body>
</html>
```